Redesign Of Hotel Coupon/Voucher 8.5 x 11

I would like to redesign my voucher.

Please provide me a color flyer design but one that would be easy on printing costs...for example printing from home computer/printer.

I would like to see some color designs...maybe some black and white and also full graphics and even basic like the plum tally voucher I provided as a sample. The 2 night hotel stay is the voucher I need to redesign...

Target Market(s)

Consumers

Industry/Entity Type

Hotel

Requirements
Must have
• exact text in current designs---look official, credible and trust worthy
Nice to have
• I would like to redesign my voucher.
• Please provide me a color flyer design but one that would be easy on printing costs...for example printing from home computer/printer.
• I would like to see some color designs...maybe some black and white and also full graphics and even basic like the plum tally voucher I provided as a sample. The 2 night hotel stay is the voucher I need to redesign...
Should not have

```html
<!DOCTYPE html>
<html lang="en">
<head>
<meta charset="utf-8">
<title>Gift Voucher – 2 Night Hotel Stay</title>
<link href="https://fonts.googleapis.com/css2?family=Pinyon+Script&family=Raleway:wght@300&family=Arimo:ital,wght@0,400;0,700;1,400;1,700&family=Roboto+Condensed:wght@400;700&family=Montserrat:wght@600;700&display=swap" rel="stylesheet">
<style>
:root{
  --page:#e6e7e9;
  --gold:#d4ab0c;
  --night-top:#1a130e;
  --night-mid:#4a3624;
  --teal:#3b98a4;
  --ink:#1e1e1e;
  --white:#ffffff;
  --navy:#0f1d2b;
  --navy-deep:#0a141f;
  --pool-top:#d6dde2;
  --pool-low:#7fc4d6;
}
*{box-sizing:border-box;margin:0;padding:0}
html,body{width:1200px;height:1085px;overflow:hidden;background:var(--page)}
.voucher{position:absolute;left:200px;top:26px;width:800px;height:1033px;overflow:hidden;font-family:"Arimo",Arial,sans-serif;color:var(--ink)}
.scene-night{position:absolute;left:0;top:0;width:800px;height:494px;background:radial-gradient(ellipse at 62% 8%,#8a6a48 0%,var(--night-mid) 35%,var(--night-top) 80%),var(--night-top)}
.scene-pool{position:absolute;left:0;top:520px;width:800px;height:259px;background:linear-gradient(180deg,var(--pool-top) 0%,#cfd8dc 45%,#b9dbe4 70%,var(--pool-low) 100%)}
.scene-sea{position:absolute;left:0;top:779px;width:800px;height:254px;background:linear-gradient(180deg,#1d2f3f 0%,var(--navy) 35%,var(--navy-deep) 100%)}
.compliments{position:absolute;left:80px;top:50px;width:174px;text-align:center;color:var(--white);font-size:12.5px;line-height:13px;letter-spacing:.3px}
.recipient{position:absolute;left:80px;top:84px;width:174px;height:173px;background:var(--white);border:5px solid var(--gold)}
.recipient-field{position:absolute;left:14px;right:14px;text-align:center;font-family:"Montserrat",sans-serif;font-weight:700;font-size:9.5px;color:#8a6a10;text-decoration:underline}
.recipient-line{position:absolute;left:14px;right:14px;height:1px;background:#555}
.title-script{position:absolute;left:279px;top:116px;font-family:"Pinyon Script",cursive;font-weight:400;font-size:52px;color:var(--gold);line-height:1}
.title-main{position:absolute;left:279px;top:178px;font-family:"Raleway",sans-serif;font-weight:300;font-size:44px;color:var(--white);letter-spacing:-.5px;line-height:1}
.destinations{position:absolute;left:48px;top:274px;width:704px;height:207px;display:grid;grid-template-columns:repeat(6,1fr);grid-template-rows:repeat(9,1fr);border:2px solid var(--gold);background:rgba(20,14,8,.45)}
.destinations span{display:flex;align-items:center;justify-content:center;text-align:center;border:1.5px solid var(--gold);color:var(--white);font-family:"Roboto Condensed",sans-serif;font-size:10.5px;line-height:8px;padding:0 2px}
.destinations .dest-head{grid-column:span 2;font-family:"Montserrat",sans-serif;font-weight:700;font-size:13px;letter-spacing:.5px;background:#000}
.band{position:absolute;left:0;top:494px;width:800px;height:26px;background:var(--teal)}
.band-tab{position:absolute;top:494px;height:26px;display:flex;align-items:center;justify-content:center;font-family:"Montserrat",sans-serif;font-weight:700;font-size:13px;color:var(--ink);letter-spacing:.3px}
.band-tab.gold{background:var(--gold)}
.redeem{position:absolute;left:80px;top:533px;width:192px;font-size:8.4px;line-height:14.5px}
.redeem em{font-weight:700}
.redeem .addr{padding-left:20px;font-style:italic;font-weight:700;line-height:11.3px}
.redeem .note{margin-top:11px;line-height:11.3px}
.redeem .ids{margin-top:6px;font-family:"Montserrat",sans-serif;font-weight:600;font-size:8px;line-height:9.5px}
.redeem .fine{margin-top:4px;font-size:6.8px;line-height:8.8px;width:240px}
.pay{position:absolute;font-size:10.5px}
.box{position:absolute;width:19px;height:19px;border:1.5px solid #222;background:rgba(255,255,255,.4)}
.rule{position:absolute;height:1px;background:#333}
.label{position:absolute;font-size:10.5px}
.ship-head{position:absolute;left:521px;top:649px;width:231px;height:24px;background:var(--gold);display:flex;align-items:center;justify-content:center;font-family:"Montserrat",sans-serif;font-weight:700;font-size:13px}
.terms{position:absolute;left:57px;top:790px;width:688px;color:var(--white);font-family:"Roboto Condensed",sans-serif;font-weight:700;font-size:7.3px;line-height:11.3px;text-align:justify;text-transform:uppercase}
.terms b{font-size:16px;letter-spacing:.2px;margin-right:6px}
</style>
</head>
<body>
<main class="voucher">
  <div class="scene-night" role="img" aria-label="Night photo of a resort with glowing lights over the sea"></div>
  <div class="scene-pool" role="img" aria-label="Photo of a lit hotel swimming pool at dusk, faded under the form"></div>
  <div class="scene-sea" role="img" aria-label="Dark photo of the sea at night behind the terms"></div>

  <p class="compliments">THIS CERTIFICATE IS<br>COMPLIMENTS OF :</p>
  <div class="recipient">
    <span class="recipient-field" style="top:12px">NAME</span>
    <span class="recipient-line" style="top:48px"></span>
    <span class="recipient-field" style="top:66px">PHONE NUMBER</span>
    <span class="recipient-line" style="top:101px"></span>
    <span class="recipient-field" style="top:120px">E-MAIL ADDRESS</span>
    <span class="recipient-line" style="top:155px"></span>
  </div>

  <h1 class="title-script">Gift Voucher</h1>
  <h2 class="title-main">2 NIGHT HOTEL STAY</h2>

  <section class="destinations">
    <span class="dest-head">DESTINATIONS AVAILABLE:</span><span>ANAHEIM</span><span>CA, ATLANTA</span><span>GA, ATLANTIC CITY</span><span>NJ, BRANSON</span>
    <span>MO, CANCUN</span><span>MX, CHARLESTON</span><span>SC, COEUR D'ALENE</span><span>ID, DAYTONA BEACH</span><span>FL, DESTIN</span><span>FL, FT. LAUDERDALE</span>
    <span>FL, FT. MEYERS</span><span>FL, GATLINBURG</span><span>TN, HILTON HEAD</span><span>SC, HONOLULU</span><span>HI, KISSIMMEE</span><span>FL, LAKE TAHOE</span>
    <span>CA, LAS VEGAS</span><span>NV, MYRTLE BEACH</span><span>SC, NIAGARA FALLS/<br>BUFFALO AREA</span><span>NY, ORLANDO</span><span>FL, ORMOND BEACH</span><span>FL, PALM SPRINGS</span>
    <span>CA, PIGEON FORGE</span><span>TN, ST. PETERSBURG</span><span>FL, SAN ANTONIO</span><span>TX, SAN DIEGO</span><span>CA, SAN FRANSISCO</span><span>CA, SEDONA</span>
    <span>AZ, SONOMA<br>WINE COUNTRY</span><span>CA, ST. GEORGE</span><span>UT, TAMPA</span><span>FL, WILLIAMSBURG</span><span>WA, WINCONSIN DELLS</span><span>WI, TALLAHASSEE</span>
    <span>FL, AUGUSTA</span><span>GA, COLUMBIA</span><span>SC, NEWYORK</span><span>NY, FLORENCE</span><span>SC, WASHINGTON</span><span>DC, CHICAGO</span>
    <span>IL, SALT LAKE CITY</span><span>UT, HOLLYWOOD</span><span>CA, DAYTON</span><span>OH, TUCSON</span><span>AZ, NIAGARA FALLS</span><span>WA, PORTLAND</span>
    <span>ON/CAN, SEATTLE</span><span>OR, ANTIOCH</span><span>CA, SAN MATEO</span><span>CA, BRUNSWIK</span><span>GA, NASHVILLE</span><span>TN,</span>
  </section>

  <div class="band"></div>
  <div class="band-tab gold" style="left:48px;width:211px">3 WAYS TO REDEEM</div>
  <div class="band-tab" style="left:278px;width:220px">PAYMENT INFORMATION</div>
  <div class="band-tab gold" style="left:518px;width:231px">BILLING INFORMATION</div>

  <section class="redeem">
    <p>1. For expedited redemption go to:</p>
    <p style="padding-left:10px"><em><i>www.TripPerksForYou.com</i></em></p>
    <p>2. Fax* certificate to: <em><i>1-888-555-0142</i></em></p>
    <p>3. Mail* to:</p>
    <p class="addr">Redemption Center<br>4410 Harbor View Rd Ste B #210<br>Lakeview, Ca 90000</p>
    <p class="note">Simply fill out the form on this certificate and enclose payment of U.S. $14.95. Vista Card, Meridian Card, Amcard, Diversa, Debit Card, Check Card, Check &amp; Money Orders are all accepted.</p>
    <p class="ids">CERTIFICATE ID &nbsp;&nbsp;&nbsp;&nbsp;: -10002<br>EXPIRATION DATE &nbsp;: 04/08/2017</p>
    <p class="fine">*Redemption Center" will appear on your billing statement.<br>Make checks and money orders payable to: "Redemption Center"<br>* You will receive your information by mail within 10 days.<br>** Last 3 digits on back of card (4 digits on front of Amcard).</p>
  </section>

  <p class="pay" style="left:292px;top:532px">Payment Method:</p>
  <span class="box" style="left:293px;top:560px"></span><span class="label" style="left:319px;top:564px">Check</span>
  <span class="box" style="left:293px;top:582px"></span><span class="label" style="left:319px;top:586px">Vista Card</span>
  <span class="box" style="left:293px;top:605px"></span><span class="label" style="left:319px;top:609px">Amcard</span>
  <span class="box" style="left:382px;top:560px"></span><span class="label" style="left:407px;top:564px">Money Order</span>
  <span class="box" style="left:382px;top:582px"></span><span class="label" style="left:407px;top:586px">Meridian Card</span>
  <span class="box" style="left:382px;top:605px"></span><span class="label" style="left:407px;top:609px">Diversa Card</span>

  <span class="label" style="left:292px;top:640px">Name On Card</span><span class="label" style="left:375px;top:640px">:</span><span class="rule" style="left:382px;top:652px;width:112px"></span>
  <span class="label" style="left:292px;top:663px">Card # (16 digits)</span><span class="label" style="left:375px;top:663px">:</span><span class="rule" style="left:382px;top:675px;width:112px"></span>
  <span class="label" style="left:292px;top:686px">Expiration Date</span><span class="label" style="left:375px;top:686px">:</span><span class="rule" style="left:382px;top:698px;width:55px"></span><span class="label" style="left:437px;top:686px">/</span><span class="rule" style="left:443px;top:698px;width:51px"></span>
  <span class="label" style="left:292px;top:709px">CV2#**</span><span class="label" style="left:375px;top:709px">:</span><span class="rule" style="left:382px;top:721px;width:112px"></span>
  <span class="label" style="left:294px;top:738px;font-style:italic;font-weight:700">I agree to terms and conditions</span>
  <span class="label" style="left:294px;top:754px;font-style:italic;font-weight:700">Signature :</span><span class="rule" style="left:355px;top:766px;width:139px"></span>

  <span class="label" style="left:521px;top:526px">Name</span><span class="label" style="left:565px;top:526px">:</span><span class="rule" style="left:573px;top:538px;width:176px"></span>
  <span class="label" style="left:521px;top:541px">Address</span><span class="label" style="left:565px;top:541px">:</span><span class="rule" style="left:573px;top:553px;width:176px"></span>
  <span class="label" style="left:521px;top:556px">City</span><span class="label" style="left:565px;top:556px">:</span><span class="rule" style="left:573px;top:568px;width:176px"></span>
  <span class="label" style="left:521px;top:571px">State</span><span class="label" style="left:565px;top:571px">:</span><span class="rule" style="left:573px;top:583px;width:176px"></span>
  <span class="label" style="left:521px;top:586px">Zip Code</span><span class="label" style="left:565px;top:586px">:</span><span class="rule" style="left:573px;top:598px;width:176px"></span>
  <span class="label" style="left:521px;top:601px">Country</span><span class="label" style="left:565px;top:601px">:</span><span class="rule" style="left:573px;top:613px;width:176px"></span>
  <span class="label" style="left:521px;top:616px">Phone</span><span class="label" style="left:565px;top:616px">:</span><span class="rule" style="left:573px;top:628px;width:176px"></span>
  <span class="label" style="left:521px;top:631px">Email</span><span class="label" style="left:565px;top:631px">:</span><span class="rule" style="left:573px;top:643px;width:176px"></span>

  <div class="ship-head">SHIPPING INFORMATION</div>
  <span class="label" style="left:521px;top:678px">Name</span><span class="label" style="left:565px;top:678px">:</span><span class="rule" style="left:573px;top:690px;width:176px"></span>
  <span class="label" style="left:521px;top:693px">Address</span><span class="label" style="left:565px;top:693px">:</span><span class="rule" style="left:573px;top:705px;width:176px"></span>
  <span class="label" style="left:521px;top:708px">City</span><span class="label" style="left:565px;top:708px">:</span><span class="rule" style="left:573px;top:720px;width:176px"></span>
  <span class="label" style="left:521px;top:723px">State</span><span class="label" style="left:565px;top:723px">:</span><span class="rule" style="left:573px;top:735px;width:176px"></span>
  <span class="label" style="left:521px;top:738px">Zip Code</span><span class="label" style="left:565px;top:738px">:</span><span class="rule" style="left:573px;top:750px;width:176px"></span>
  <span class="label" style="left:521px;top:753px">Country</span><span class="label" style="left:565px;top:753px">:</span><span class="rule" style="left:573px;top:765px;width:176px"></span>

  <p class="terms"><b>Terms &amp; Conditions</b>This certificate will be considered void if bartered or purchased for legal tender by the recipient. This certificate is valid for a reservation request form offering 2 adults 21 years of age and older plus up to 2 children under the age of 18, 2 nights of hotel accommodations in the city of their choice of available cities. The cost to activate this certificate to receive the reservation request form is just a one-time non-refundable $14.95 processing fee. The cost upon requesting reservations is just a tax &amp; fee deposit of $33 per night. Taxes &amp; fees usually range from $12-$33 per night depending on when and where you travel to. If the taxes &amp; fees are less than the $33 per night the difference will be refunded after travel is completed. 30 days advance reservation notice is required. In order to guarantee that you will show up to your booked reservation you will be required to pay a refundable $50 "reservation guarantee deposit". If you send in your travel dates, etc and you do not end up traveling then the reservation guarantee deposit will not be refundable. 7 days before and after holidays and conventions are not available. This offer is valid 7 days a week subject to availability. Friday and Saturday nights will require a surcharge of $20 per night. A $5 per person per night surcharge is enforced for each child up to 2 children under the age of 18. This offer is not valid for group travel. The recipient of this certificate is responsible for all expenses including but not limited to: transfers, food, gratuities, all pertinent fees, taxes, hotel surcharges, resort fees and any other miscellaneous expenses. If you activate this certificate online you will be able to instantly print your reservation request form. If you cannot print your own reservation request form we will mail it to you. You should receive it in the mail within 14 days. This certificate cannot be combined with any other promotional vacation offer. The expiration date on this certificate pertains only to activation of this certificate and not actual travel. You must activate this certificate by the expiration date printed on this certificate in order to receive the reservation request form. You must fill out the reservation request form with your destination choices and arrival dates and mail it to our fulfillment department within 6 months after activation, however travel can be completed within 12 months after activation. You will be required to give the travel agency multiple arrival dates and destinations. Only one 2 night hotel certificate per household per year. This certificate has no cash surrender value. Void if discontinued and where prohibited by law. The terms of this offer are subject to change without notice. Do not rely upon representations other than what is printed on this certificate or the reservation request form. CST # 5500417</p>
</main>
</body>
</html>
```